Tallow Creek Biotics - Business Card Design

Business Card Brief;
We require a design for a business card template for our business “Tallow Creek Biotics”.
We are a firm that manufacture positive microbial formulations to enhance agricultural legume crops such as lucence, soy beans and faba beans. We also manufacture microbial formulations that aid in composting of waste organic waste to use as a natural fertilizer.
We are seeking a business card design that portrays a clean, professional organisation dedicated to enhancing nature and sustainable farming techniques.
Our website is www.soilvantage.com.au
Here is a link to a drawing of a soybean plant. One of our main products is used to help grow these. I offer it an an example of the type of graphic that might be used on the card, but will leave you to create your own design; https://pixelvaultimages.com/482915066/stock-illustration-soybean-plant-on-a-white.html
Two cards are required;
--------------------------------------------------------------------
Card #1
Cody R Whitfield
Executive Chairman
Mobile: 0471 583204
Email: cody@soilvantage.com.au
---------------------------------------------------------------------------
Card #2
Lachlan P Doyce
Chief Financial & Operating Officer
Mobile: 0456 792418
Email lachlan@soilvantage.com.au

Many thanks
Lachlan Doyce

Industry/Entity Type

Agriculture

Colors

Designer to choose colors to be used in the design.

Requirements
Must have
• An elegant design that demonstrates our commitment to enhancing nature.

```html
<!DOCTYPE html>
<html lang="en">
<head>
<meta charset="utf-8">
<title>Tallow Creek Biotics – Business Cards</title>
<link rel="stylesheet" href="https://fonts.googleapis.com/css2?family=Montserrat:wght@300;400;700&display=swap">
<style>
  :root {
    --page: #ffffff;
    --card-light: #f5f7f6;
    --charcoal: #3c3c3c;
    --ink: #333333;
    --leaf: #8cb443;
    --leaf-dark: #6aa232;
    --leaf-bright: #a8c93b;
    --logo-text: #e6e6e6;
    --logo-mark: #5c5a5a;
  }
  html, body {
    margin: 0;
    padding: 0;
    width: 1200px;
    height: 1200px;
    overflow: hidden;
    background: var(--page);
    font-family: "Montserrat", sans-serif;
  }
  .card {
    position: absolute;
    left: 221px;
    width: 757px;
    height: 454px;
    background: var(--card-light);
    overflow: hidden;
  }
  .card--chairman-top { top: 110px; }
  .card--second { top: 642px; }
  .card__panels {
    position: absolute;
    inset: 0;
  }
  .brand {
    position: absolute;
    left: 52px;
    top: 282px;
    display: flex;
    align-items: center;
    gap: 14px;
  }
  .brand__dot {
    width: 64px;
    height: 64px;
    border-radius: 50%;
    background: var(--logo-mark);
  }
  .brand__name {
    color: var(--logo-text);
    font-weight: 300;
    font-size: 27px;
    line-height: 32px;
  }
  .person {
    position: absolute;
    left: 300px;
    width: 446px;
    text-align: center;
  }
  .person__name {
    margin: 0;
    font-size: 44px;
    line-height: 1;
    color: var(--ink);
    font-weight: 300;
    letter-spacing: -0.5px;
    white-space: nowrap;
  }
  .person__name strong { font-weight: 700; }
  .person__title {
    margin: 10px 0 0;
    font-size: 13.5px;
    letter-spacing: 2px;
    color: var(--leaf);
    font-weight: 400;
    white-space: nowrap;
  }
  .person__title--wide { font-size: 15.5px; letter-spacing: 2.6px; }
  .contacts {
    position: absolute;
    left: 393px;
    top: 209px;
    margin: 0;
    padding: 0;
    list-style: none;
  }
  .contacts__item {
    display: flex;
    align-items: center;
    height: 36px;
    margin-bottom: 20px;
    font-size: 17.5px;
    color: var(--ink);
  }
  .contacts__item:last-child { margin-bottom: 0; }
  .contacts__icon {
    width: 35px;
    height: 35px;
    margin-right: 14px;
    flex: none;
  }
  .sprout {
    position: absolute;
    right: 0;
    bottom: 0;
    width: 150px;
    height: 246px;
    background: linear-gradient(200deg, rgba(245,247,246,0) 10%, rgba(140,180,67,0.28) 60%, rgba(106,162,50,0.45) 100%);
  }
</style>
</head>
<body>

<svg width="0" height="0" style="position:absolute">
  <defs>
    <linearGradient id="leaf-band" x1="0" y1="0" x2="0" y2="1">
      <stop offset="0" stop-color="#a8c93b"/>
      <stop offset="1" stop-color="#6aa232"/>
    </linearGradient>
    <symbol id="icon-phone" viewBox="0 0 36 36">
      <circle cx="18" cy="18" r="17.5" fill="#8cb443"/>
      <path d="M12.5 9.5c1-.6 2-.4 2.6.6l1.6 2.7c.5.9.3 1.9-.5 2.5l-1.3 1c.9 2 2.5 3.7 4.5 4.6l1-1.3c.6-.8 1.7-1 2.5-.5l2.7 1.6c1 .6 1.2 1.7.6 2.6l-.9 1.3c-.8 1.1-2.2 1.6-3.5 1.2-5.1-1.6-9.1-5.6-10.7-10.7-.4-1.3.1-2.7 1.2-3.5z" fill="#ffffff"/>
    </symbol>
    <symbol id="icon-mail" viewBox="0 0 36 36">
      <circle cx="18" cy="18" r="17.5" fill="#8cb443"/>
      <rect x="10" y="12" width="16" height="12" rx="1" fill="#ffffff"/>
      <path d="M10.5 12.8 18 18.8l7.5-6M10.5 23.2l5.4-5.2M25.5 23.2l-5.4-5.2" fill="none" stroke="#8cb443" stroke-width="1.3"/>
    </symbol>
    <symbol id="icon-globe" viewBox="0 0 36 36">
      <circle cx="18" cy="18" r="17.5" fill="#8cb443"/>
      <circle cx="18" cy="18" r="8" fill="none" stroke="#ffffff" stroke-width="1.6"/>
      <ellipse cx="18" cy="18" rx="3.5" ry="8" fill="none" stroke="#ffffff" stroke-width="1.4"/>
      <path d="M10 18h16M11.5 13.5h13M11.5 22.5h13" fill="none" stroke="#ffffff" stroke-width="1.3"/>
    </symbol>
  </defs>
</svg>

<section class="card card--chairman-top" aria-label="Business card – Lachlan P Doyce">
  <svg class="card__panels" viewBox="0 0 757 454" width="757" height="454" aria-hidden="true">
    <polygon points="211,0 272,0 362,454 356,454" fill="url(#leaf-band)"/>
    <polygon points="0,0 211,0 357,454 0,454" fill="#3c3c3c"/>
  </svg>
  <div class="brand">
    <span class="brand__dot"></span>
    <span class="brand__name">Tallow Creek<br>Biotics</span>
  </div>
  <div class="person" style="top:94px">
    <h1 class="person__name">Lachlan P <strong>Doyce</strong></h1>
    <p class="person__title">CHIEF FINANCIAL &amp; OPERATING OFFICER</p>
  </div>
  <ul class="contacts">
    <li class="contacts__item"><svg class="contacts__icon"><use href="#icon-phone"/></svg>0456 792418</li>
    <li class="contacts__item"><svg class="contacts__icon"><use href="#icon-mail"/></svg>cody@soilvantage.com.au</li>
    <li class="contacts__item"><svg class="contacts__icon"><use href="#icon-globe"/></svg>lachlan@soilvantage.com.au</li>
  </ul>
  <div class="sprout" role="img" aria-label="Illustration of a young soybean sprout with leaves"></div>
</section>

<section class="card card--second" aria-label="Business card – Cody R Whitfield">
  <svg class="card__panels" viewBox="0 0 757 454" width="757" height="454" aria-hidden="true">
    <polygon points="211,0 272,0 362,454 356,454" fill="url(#leaf-band)"/>
    <polygon points="0,0 211,0 357,454 0,454" fill="#3c3c3c"/>
  </svg>
  <div class="brand">
    <span class="brand__dot"></span>
    <span class="brand__name">Tallow Creek<br>Biotics</span>
  </div>
  <div class="person" style="top:96px">
    <h1 class="person__name">Cody R <strong>Whitfield</strong></h1>
    <p class="person__title person__title--wide">EXECUTIVE CHAIRMAN</p>
  </div>
  <ul class="contacts">
    <li class="contacts__item"><svg class="contacts__icon"><use href="#icon-phone"/></svg>0471 583204</li>
    <li class="contacts__item"><svg class="contacts__icon"><use href="#icon-mail"/></svg>cody@soilvantage.com.au</li>
    <li class="contacts__item"><svg class="contacts__icon"><use href="#icon-globe"/></svg>www.soilvantage.com.au</li>
  </ul>
  <div class="sprout" role="img" aria-label="Illustration of a young soybean sprout with leaves"></div>
</section>

</body>
</html>
```